Real Estate Templates in Canva

I need someone to create a robust set of Canva template designs for my real estate company team, to streamline content. I need a catalog for my agents to easily go in and pick from different designs and customize for themselves. The correct candidate can emulate the style found on these sites., and in the attached images. I have also uploaded logos to be used.(https://www.tundrahomesgroup.com/) and (https://meetcalverly.com/)

I want a fantastic sharp style that has great color blend and is attractive and matches my brand well.

The correct candidate will have access to my Canva Brand Kit and build templates inside of my account.

Also attached is a screenshot of my main color codes

The types of templates can include, but not be limited to the following:
BOTH DIGITAL FOR SOCIAL MEDIA AND PRINT VERSIONS
Listings flyers
Clients testimonials
market stats
open houses
Realtor Insights
Realtor analysis
sold properties
new listing properties
under contract properties
coming soon properties
Bullet points summarizing key data
Photo of the client at closing
Photo of the client at their home

Property Listing Template:

Description of the property
High-quality images
Key features and amenities
Open House Invitation:

Date, time, and location details
Compelling visuals of the property
Call-to-action for attendance
Just Sold Announcement:

Property details (address, price, etc.)
Celebratory message
Testimonials from satisfied clients
Testimonial Template:

Client testimonial
Photo of the client (with permission)
Brief background or story
Market Update Infographic:

Visual representation of current market trends
Realtor's insights and analysis
Buyer's Guide:

Step-by-step guide for homebuyers
Infographics explaining the buying process
Tips and advice for a successful purchase
Seller's Guide:

Information on preparing a home for sale
Infographics on the selling process
Tips for maximizing property value
Seasonal Greetings Template:

Personalized message for clients
Festive visuals or themes
Wishes for a successful year ahead
Neighborhood Highlight:

Showcase a specific neighborhood
Key attractions, schools, amenities
Testimonials from residents (if available)
Behind-the-Scenes:

Photos or videos of the realtor at work
Personalized messages about the real estate process
Humanizing content to connect with the audience
Infographic: Benefits of Working with a Realtor:

Visual representation of the advantages
Statistics or data supporting the benefits
Clear, concise points for easy consumption
Interactive Polls or Quizzes:

Engage the audience with fun polls
Real estate-related quizzes
Encourage interaction and sharing
Client Appreciation Post:

Thanking clients for their trust
Sharing success stories
Expressing gratitude with visuals
Video Tour Teaser:

Sneak peek of a property tour
Create excitement and anticipation

Target Market(s)

General Population ages 30-70

Requirements
Must have
• 60 plus designs
Nice to have
• 100 plus designs

```html
<!DOCTYPE html>
<html lang="en">
<head>
<meta charset="utf-8">
<title>Tundra Homes Group – Social Templates</title>
<link rel="stylesheet" href="https://fonts.googleapis.com/css2?family=Open+Sans:ital,wght@0,400;0,600;0,700;0,800;1,600&family=Yellowtail&display=swap">
<style>
:root{
  --bg:#e8e8e8;
  --orange:#f39530;
  --orange-deep:#e98a2b;
  --ink:#231f20;
  --night:#1a1a1a;
  --white:#ffffff;
}
*{box-sizing:border-box;margin:0;padding:0}
html,body{width:1200px;height:908px;overflow:hidden;background:var(--bg);font-family:"Open Sans",sans-serif}
.board{position:relative;width:1200px;height:908px}
.tile{position:absolute;overflow:hidden}

/* listing cards */
.listing{width:323px;height:323px;background:var(--white)}
.listing__head{position:absolute;left:0;top:0;width:100%;height:111px;background:var(--orange)}
.listing__title{position:absolute;left:25px;top:18px;max-width:188px;color:var(--ink);font-weight:700;font-size:18px;line-height:16px;text-transform:uppercase;letter-spacing:-.2px;white-space:nowrap}
.listing__title--compact{top:24px;font-size:15px;line-height:15px;letter-spacing:-.4px}
.listing__type{position:absolute;left:25px;top:58px;color:var(--ink);font-size:10.5px;line-height:13px}
.listing__type b{font-weight:700}
.listing__facts{position:absolute;left:221px;top:22px;color:var(--white);font-weight:700;font-size:8.4px;line-height:11.2px;text-transform:uppercase}
.listing__photo{position:absolute;left:0;top:111px;width:100%;height:160px}
.photo--autumn{background:linear-gradient(180deg,#e9a24a 0%,#c27a3a 25%,#2f4a34 55%,#3b3b40 75%,#6b5a4a 100%)}
.photo--newbuild{background:linear-gradient(180deg,#d9dde0 0%,#8b919a 35%,#cfcac0 60%,#b49c80 100%)}
.listing__peaks{position:absolute;left:0;top:200px;width:323px;height:71px}
.listing__foot{position:absolute;left:0;top:271px;width:100%;height:52px;background:var(--white)}
.brand{position:absolute;display:flex;align-items:center;gap:6px;color:var(--orange);font-weight:600;font-size:14px;letter-spacing:.3px;text-transform:uppercase}
.brand__dot{width:26px;height:26px;border-radius:50%;background:var(--orange)}
.listing .brand{left:27px;top:12px}
.listing__price{position:absolute;right:26px;top:9px;color:var(--orange);font-weight:600;font-size:23px}

/* testimonial */
.review{width:322px;height:322px;background:var(--orange)}
.review__stars{position:absolute;left:108px;top:50px;width:106px;height:20px}
.review__quote{position:absolute;left:48px;top:80px;width:226px;color:var(--white);font-style:italic;font-weight:600;font-size:10.6px;line-height:14.2px;text-align:center}
.review__name{position:absolute;right:50px;top:212px;color:var(--white);font-weight:700;font-size:13px}
.review__hills{position:absolute;left:0;bottom:0;width:322px;height:110px}

/* open house */
.invite{width:322px;height:322px;background:var(--night)}
.invite__frame{position:absolute;left:19px;top:24px;width:283px;height:277px;border:3px solid var(--white);z-index:2}
.invite__script{position:absolute;left:0;top:28px;width:100%;text-align:center;color:var(--orange);font-family:"Yellowtail",cursive;font-weight:400;font-size:46px;line-height:1}
.invite__label{position:absolute;left:0;top:89px;width:100%;text-align:center;color:var(--white);font-weight:700;font-size:11px;letter-spacing:8px;padding-left:8px}
.invite__meta{position:absolute;left:38px;top:115px;display:flex;gap:16px;color:var(--white);font-weight:600;font-size:8.4px}
.invite__meta span{display:flex;align-items:center;gap:3px}
.invite__photo{position:absolute;left:0;top:146px;width:100%;height:101px;background:linear-gradient(180deg,#d9954a 0%,#3c5a3a 35%,#33333a 65%,#7a6450 100%)}
.invite .brand{left:0;right:0;top:259px;justify-content:center;font-size:13px}
.invite .brand__dot{width:22px;height:22px}

/* key points */
.points{width:325px;height:322px;background:var(--orange)}
.points__list{position:absolute;left:30px;top:50px;list-style:none}
.points__list li{position:relative;padding-left:19px;color:var(--white);font-weight:700;font-size:11.5px;line-height:11px;margin-bottom:16px}
.points__list li::before{content:"";position:absolute;left:0;top:2px;width:8px;height:8px;background:var(--white)}
.points__photo{position:absolute;left:179px;top:0;width:146px;height:322px;background:linear-gradient(180deg,#7b8a96 0%,#5b6470 30%,#c9c4ba 52%,#b9a286 75%,#cdb89b 100%)}
</style>
</head>
<body>
<main class="board">

  <section class="tile listing" style="left:91px;top:94px">
    <div class="listing__head">
      <h2 class="listing__title">42 W Alder Court<br>Active</h2>
      <p class="listing__type"><b>HOUSE</b><br>3/2.00/3 • 344.83 SQ. FT.<br>0.560 ACRES</p>
      <p class="listing__facts">3 Bedrooms<br>2.00 Bathrooms<br>3 Garage<br>345 Sq. Feet<br>0.560 Acres<br>1986</p>
    </div>
    <div class="listing__photo photo--autumn" role="img" aria-label="Two-storey house among autumn trees at dusk"></div>
    <svg class="listing__peaks" viewBox="0 0 323 71" aria-hidden="true"><polygon points="0,60 56,14 101,54 116,36 161,71 0,71" fill="#fff"/></svg>
    <div class="listing__foot">
      <div class="brand"><span class="brand__dot"></span>Tundra Homes</div>
      <p class="listing__price">$640,000</p>
    </div>
  </section>

  <section class="tile listing" style="left:435px;top:94px">
    <div class="listing__head" style="height:112px">
      <h2 class="listing__title listing__title--compact">118 Elk Crest Place<br><span style="font-size:18px">Active</span></h2>
      <p class="listing__type" style="top:60px"><b>HOUSE<br>3/2.00/2 • 1561 SQ. FT.<br>0.220 ACRES</b></p>
      <p class="listing__facts" style="left:219px">3 Bedrooms<br>2.00 Bathrooms<br>2 Garage<br>1,561 Sq. Feet<br>0.220 Acres<br>2023</p>
    </div>
    <div class="listing__photo photo--newbuild" style="top:112px;height:159px" role="img" aria-label="New single-storey house with covered porch and garage"></div>
    <svg class="listing__peaks" viewBox="0 0 323 71" aria-hidden="true"><polygon points="0,60 56,14 101,54 116,36 161,71 0,71" fill="#fff"/></svg>
    <div class="listing__foot">
      <div class="brand"><span class="brand__dot"></span>Tundra Homes</div>
      <p class="listing__price">$595,000</p>
    </div>
  </section>

  <section class="tile review" style="left:789px;top:94px">
    <svg class="review__stars" viewBox="0 0 106 20" aria-label="Five stars" role="img">
      <defs><polygon id="star" points="8,0 10.2,5.8 16,6 11.5,9.8 13,16 8,12.6 3,16 4.5,9.8 0,6 5.8,5.8"/></defs>
      <use href="#star" x="0" y="2" fill="#fff"/><use href="#star" x="22" y="2" fill="#fff"/><use href="#star" x="44" y="2" fill="#fff"/><use href="#star" x="66" y="2" fill="#fff"/><use href="#star" x="88" y="2" fill="#fff"/>
    </svg>
    <p class="review__quote">"Tundra Homes Group is the one and only compay that I would choose work with for my real estate needs in Calverly. Working with them was like working with family! I worked with them to help sell my mother's house and I have never felt more comfortable and confident in a transaction. If I could give 10 stars, I would!"</p>
    <p class="review__name">Dana Whitfield</p>
    <svg class="review__hills" viewBox="0 0 322 110" aria-hidden="true">
      <path d="M0,62 C40,30 80,10 110,12 C150,15 170,60 205,62 C235,64 250,30 280,30 C300,30 312,38 322,42 L322,110 L0,110 Z" fill="var(--orange-deep)"/>
    </svg>
  </section>

  <section class="tile invite" style="left:232px;top:457px">
    <div class="invite__frame"></div>
    <h2 class="invite__script">Open Home</h2>
    <p class="invite__label">INVITE</p>
    <div class="invite__meta">
      <span><svg width="9" height="9" viewBox="0 0 9 9" aria-hidden="true"><rect x=".5" y="1.5" width="8" height="7" fill="none" stroke="#f39530"/><rect x=".5" y="1.5" width="8" height="2" fill="#f39530"/></svg>20th May 2024</span>
      <span><svg width="7" height="9" viewBox="0 0 7 9" aria-hidden="true"><path d="M3.5 0C1.6 0 0 1.5 0 3.4 0 5.8 3.5 9 3.5 9S7 5.8 7 3.4C7 1.5 5.4 0 3.5 0z" fill="#f39530"/><circle cx="3.5" cy="3.4" r="1.2" fill="#1a1a1a"/></svg>123Anywhere City, ANy City 1203</span>
    </div>
    <div class="invite__photo" role="img" aria-label="Lit house among autumn trees at dusk"></div>
    <div class="brand"><span class="brand__dot"></span>Tundra Homes</div>
  </section>

  <section class="tile points" style="left:598px;top:455px">
    <ul class="points__list">
      <li>Bullet points</li>
      <li>summarizing key</li>
      <li>data</li>
      <li>annother points</li>
      <li>summarizing<br>key data</li>
      <li>lorem psum<br>dolor</li>
      <li>lorem psum<br>dolor sit amet</li>
    </ul>
    <div class="points__photo" role="img" aria-label="Corner of a new house with garage and porch over a dirt yard"></div>
  </section>

</main>
</body>
</html>
```